Harborline Security and Surveillance Business Card

Business Card Design - Company Name:Freedom Security and SurveillanceWe are a Security Systems Integrator Specializing in Security Systems/ Video Surveillance and Access Control. Our areas of expertise are:Security SystemsVideo SurveillanceAccess ControlFire Alarm SystemsNetwork CablingCellular BoostersMy input is the Front of the Card is: logo, name of Business, My Name, Phone Number, and email.Rear of Card is the 6 areas of expertise, I just dont want the front to be very busy.
Name: Tom Werner
Title: President
Email: tom@harborlinesecsys.example
website: harborlinesecsys.example

```html
<!DOCTYPE html>
<html lang="en">
<head>
<meta charset="utf-8">
<title>Harborline Security and Surveillance – Business Card</title>
<link rel="stylesheet" href="https://fonts.googleapis.com/css2?family=Poppins:wght@300;400;600&display=swap">
<style>
  :root {
    --backdrop: #2a2b2d;
    --card: #1a1b1d;
    --card-pattern: #1e1f22;
    --edge-blue: #1a6ad6;
    --accent-blue: #2a7be6;
    --silver: #b9babc;
    --text-light: #d6d7d9;
    --text-muted: #a4a5a8;
  }
  * { box-sizing: border-box; margin: 0; padding: 0; }
  html, body {
    width: 1200px; height: 960px; overflow: hidden;
    background: var(--backdrop);
    font-family: "Poppins", sans-serif;
  }
  .canvas {
    width: 1200px; height: 960px;
    display: flex; flex-direction: column;
    align-items: center; justify-content: center; gap: 56px;
  }
  .card {
    position: relative;
    width: 700px; height: 400px;
    background: var(--card);
    border-radius: 26px;
    box-shadow: 0 6px 0 var(--edge-blue), 0 18px 40px rgba(0,0,0,.55);
    overflow: hidden;
  }
  /* Services side */
  .services-side {
    display: flex; flex-direction: column;
    align-items: center; justify-content: center;
  }
  .brand {
    display: flex; align-items: center; gap: 18px;
    margin-bottom: 62px;
  }
  .brand-dot {
    width: 40px; height: 40px; border-radius: 50%;
    background: var(--silver);
  }
  .brand-name {
    font-weight: 600; font-size: 30px; letter-spacing: 1px;
    color: var(--silver); text-transform: uppercase; line-height: 1.1;
  }
  .services {
    text-align: center; font-weight: 300; font-size: 17px;
    line-height: 1.5; color: var(--text-muted);
  }
  /* Contact side */
  .contact-side .pattern {
    position: absolute; inset: 0;
    background: radial-gradient(ellipse at 60% 40%, var(--card-pattern), var(--card) 75%);
  }
  .contact {
    position: relative; height: 100%;
    display: flex; flex-direction: column;
    align-items: center; justify-content: center; text-align: center;
  }
  .contact-brand {
    font-weight: 600; font-size: 15px; letter-spacing: 1px;
    text-transform: uppercase; color: var(--accent-blue);
    margin-bottom: 22px;
  }
  .person-name {
    font-weight: 400; font-size: 32px; color: var(--accent-blue); line-height: 1.1;
  }
  .person-title {
    font-weight: 400; font-size: 18px; color: var(--text-light);
    margin-bottom: 30px;
  }
  .contact-line {
    font-weight: 300; font-size: 18px; color: var(--text-light); line-height: 1.35;
  }
</style>
</head>
<body>
<main class="canvas">
  <section class="card services-side">
    <div class="brand">
      <span class="brand-dot"></span>
      <span class="brand-name">Harborline Security<br>and Surveillance</span>
    </div>
    <p class="services">
      Security Systems • Video Surveillance • Access Control<br>
      Fire Alarm Systems • Network Cabling • Cellular Boosters
    </p>
  </section>

  <section class="card contact-side">
    <div class="pattern" role="img" aria-label="Faint tone-on-tone repeating company emblem pattern"></div>
    <div class="contact">
      <p class="contact-brand">Harborline Security and Surveillance</p>
      <h1 class="person-name">Tom Werner</h1>
      <p class="person-title">President</p>
      <p class="contact-line">tom@harborlinesecsys.example</p>
      <p class="contact-line">harborlinesecsys.example</p>
    </div>
  </section>
</main>
</body>
</html>
```